Verdant Pathworks Business Card

want the back of card to be blue- with the logo in the center
front of card- info plus logo (info being mailing address, email address, and website address )
4 different names with titles to have on cards
1) Dominic Ashvale - Owner
2) Bethany Korvuth- Customer Relationship Specialist
3) Luca Brennwick- Vice President of Sales
4) Neil Umbright- Chief Technology Officer

Target Market(s)

tech company in the government/probation office industry

Industry/Entity Type

Government Office

Contact Information for Business Card

1) Dominic Ashvale - Owner

Colors
0355a3
ffffff

Requirements
Must have
• back side should be blue, with the logo placed in the center
• front side needs to include both the logo, as well as company info (info should include website address, email address, and mailing address)

```html
<!DOCTYPE html>
<html lang="en">
<head>
<meta charset="utf-8">
<title>Verdant Pathworks Business Card</title>
<link href="https://fonts.googleapis.com/css2?family=Montserrat:wght@400;700&display=swap" rel="stylesheet">
<style>
  :root {
    --navy: #152d52;
    --stage: #bdbdbd;
    --slate: #808184;
    --ink-grey: #6d6e71;
    --white: #ffffff;
  }
  * { margin: 0; padding: 0; box-sizing: border-box; }
  html, body { width: 1200px; height: 1200px; overflow: hidden; }
  body {
    background: var(--stage);
    font-family: "Montserrat", sans-serif;
    position: relative;
  }
  .card-art { position: absolute; inset: 0; width: 1200px; height: 1200px; }
  .label { position: absolute; white-space: nowrap; }

  /* back side */
  .back-wordmark {
    left: 187px; width: 826px; top: 326px;
    text-align: center; color: var(--white);
    font-size: 46px; font-weight: 700; letter-spacing: 2px;
    text-transform: uppercase;
  }
  .back-website {
    left: 187px; width: 826px; top: 486px;
    text-align: center; color: var(--white);
    font-size: 17px; font-weight: 400; letter-spacing: 6px;
  }

  /* front side */
  .front-wordmark {
    left: 220px; width: 236px; top: 852px;
    text-align: center; color: var(--white);
    font-size: 25px; font-weight: 700; line-height: 1.15;
    text-transform: uppercase; letter-spacing: 1px;
  }
  .person-name {
    left: 589px; top: 704px;
    color: var(--white); font-size: 32px; font-weight: 700;
    text-transform: uppercase; letter-spacing: 0.3px;
  }
  .person-title {
    left: 589px; top: 754px;
    color: var(--ink-grey); font-size: 23px; font-weight: 400;
    text-transform: uppercase;
  }
  .contact-address { left: 679px; top: 917px; color: var(--ink-grey); font-size: 17px; }
  .contact-line { left: 707px; color: var(--ink-grey); font-size: 17px; }
  .contact-phone  { top: 947px; }
  .contact-fax    { top: 970px; }
  .contact-mobile { top: 992px; }
  .contact-email  { top: 1014px; }
</style>
</head>
<body>

<svg class="card-art" viewBox="0 0 1500 1500" xmlns="http://www.w3.org/2000/svg">
  <defs>
    <clipPath id="back-card-shape">
      <rect x="234" y="126" width="1032" height="604" rx="90"/>
    </clipPath>
    <clipPath id="front-card-shape">
      <rect x="231" y="763" width="1038" height="608" rx="90"/>
    </clipPath>
    <linearGradient id="trace-glow" x1="0" y1="0" x2="1" y2="0.3">
      <stop offset="0" stop-color="#1b355c" stop-opacity="0"/>
      <stop offset="0.5" stop-color="#1e3a63" stop-opacity="0.7"/>
      <stop offset="1" stop-color="#1b355c" stop-opacity="0.3"/>
    </linearGradient>
  </defs>

  <!-- back side -->
  <g class="back-card" clip-path="url(#back-card-shape)">
    <rect x="234" y="126" width="1032" height="604" fill="var(--navy)"/>
    <rect x="470" y="150" width="800" height="560" fill="url(#trace-glow)"
          role="img" aria-label="Faint circuit-trace background texture"/>
    <circle class="back-mark" cx="750" cy="320" r="58" fill="none" stroke="var(--white)" stroke-width="7"/>
  </g>

  <!-- front side -->
  <g class="front-card" clip-path="url(#front-card-shape)">
    <rect x="231" y="763" width="1038" height="608" fill="var(--white)"/>
    <path class="slate-panel" d="M231 763 L550 763 Q562 1120 775 1371 L231 1371 Z" fill="var(--slate)"/>
    <path class="navy-band" d="M563 763 L628 763 Q640 975 705 1120 L652 1160 Q575 990 563 763 Z" fill="var(--navy)"/>
    <g class="shield-lines" fill="none" stroke="var(--slate)" stroke-width="9">
      <path d="M1269 970 Q960 965 660 1166 Q720 1270 815 1371"/>
      <path d="M1269 1012 Q990 1010 750 1195 Q820 1290 905 1371"/>
      <path d="M1269 1215 Q1210 1300 1140 1371"/>
    </g>
    <rect class="name-bar" x="716" y="878" width="560" height="54" fill="var(--navy)"/>
    <circle class="front-mark" cx="422" cy="1022" r="40" fill="none" stroke="var(--white)" stroke-width="6"/>

    <!-- contact icons -->
    <g class="contact-icons" fill="var(--navy)">
      <path d="M857 1190 q4 -3 7 0 l2 5 q0 3 -3 4 q2 5 7 7 q1 -3 4 -3 l5 2 q3 3 0 7 q-4 4 -11 0 q-8 -5 -11 -13 q-2 -6 0 -9z"/>
      <rect x="859" y="1219" width="12" height="5"/>
      <rect x="855" y="1224" width="20" height="9" rx="2"/>
      <rect x="859" y="1230" width="12" height="7" fill="var(--white)" stroke="var(--navy)" stroke-width="2"/>
      <rect x="859" y="1245" width="12" height="21" rx="2"/>
      <rect x="862" y="1249" width="6" height="12" fill="var(--white)"/>
      <rect x="855" y="1277" width="22" height="14"/>
      <path d="M855 1277 L866 1286 L877 1277" fill="none" stroke="var(--white)" stroke-width="2"/>
    </g>
  </g>
</svg>

<div class="label back-wordmark">Verdant Pathworks</div>
<div class="label back-website">www.verdantpathworks.net</div>

<div class="label front-wordmark">Verdant<br>Pathworks</div>
<div class="label person-name">Dominic Ashvale</div>
<div class="label person-title">Owner</div>
<div class="label contact-address">Your Full Address Comes here</div>
<div class="label contact-line contact-phone">: (000) 000-0000</div>
<div class="label contact-line contact-fax">: (000) 000-0000</div>
<div class="label contact-line contact-mobile">: (000) 000-0000</div>
<div class="label contact-line contact-email">: info@verdantpathworks.net</div>

</body>
</html>
```